Design for a real estate wev portal

Contents and features of the site
---------------------------------
Website in 5 languages: French, Dutch, English, German, Spanish.
English name of the site: Lantern Nest Place
Main purpose of the site:
- allow people to rent their house/ appartment for flatsharing purposes.
- help people wanting to find a room in flatsharing
- help people to find additional roommates for their flatsharing
Key interaction sequence:
1. I create a "group" of people who have common interest/hobbies
2. People who have the same interests/hobbies join my group
3. I look for a house/appartment to host my group
Website structure will be the following:
- Home
- Groups
-- Look for a group
--- Join a group
-- Create a group
- Properties
-- Look for a house/appartement
-- Apply
- Sales conditions
- Contact
- My account
-- My profile
-- My groups OR my properties
Your mission
------------
The client has no graphical guidelines, simply a logo (see attached).
We need a (responsive compliant) design for the following pages (we expect PSD's from you. No HTML nor CSS):
1. homepage (see example and wireframe attached)
2. properties search result list (see wireframe attached)
3. "detailed" form for properties
4. groups search result list
5. "detailed" form for groups
6. my account page
FOR THE COMPETITION step we only expect from you the design of first 2 screens.
Based on that, we will select the designer who will win the project, and will have to design the 4 remaining screens.
Target Market(s)
B2C
Industry/Entity Type
Real Estate
Number of Pages Required
5+ page
Look and feel
Each slider illustrates characteristics of the customer's brand and the style your logo design should communicate.

```html
<!DOCTYPE html>
<html lang="en">
<head>
<meta charset="utf-8">
<title>Lantern Nest Place – Flatsharing for Everyone</title>
<link href="https://fonts.googleapis.com/css2?family=Oswald:wght@400;500&family=Roboto:wght@400;500;700&display=swap" rel="stylesheet">
<style>
:root{
  --cyan:#1bc4d8;
  --cyan-dark:#14a9bb;
  --yellow:#fdc800;
  --yellow-soft:#f7cf2a;
  --dark:#1e2024;
  --darker:#151618;
  --slate:#2b3a48;
  --white:#ffffff;
  --text-dark:#222;
  --muted:#8a8d92;
}
*{box-sizing:border-box;margin:0;padding:0}
html,body{width:1200px;height:2605px;overflow:hidden}
body{position:relative;font-family:'Roboto',sans-serif;color:var(--text-dark);background:var(--white)}
.abs{position:absolute}
h1,h2,h3,.oswald{font-family:'Oswald',sans-serif;font-weight:400}

/* HERO */
.hero{left:0;top:0;width:1200px;height:596px;background:linear-gradient(180deg,#26282c 0%,#1b1d20 60%,#23262a 100%)}
.topbar{left:0;top:0;width:1200px;height:72px;border-bottom:1px solid rgba(255,255,255,.08)}
.brand{left:170px;top:26px;display:flex;align-items:center;gap:8px;color:var(--white);font-family:'Roboto',sans-serif;font-weight:700;font-size:19px}
.brand-dot{width:12px;height:12px;border-radius:50%;background:var(--cyan)}
.social{left:832px;top:14px;display:flex;gap:9px}
.social span{width:8px;height:8px;border-radius:50%;background:var(--yellow)}
.btn-create{left:912px;top:7px;width:62px;height:28px;background:var(--cyan);color:#fff;font-size:12px;font-weight:500;display:flex;align-items:center;justify-content:center;border-radius:3px 0 0 3px}
.btn-login{left:974px;top:7px;width:58px;height:28px;background:var(--yellow);color:#222;font-size:12px;font-weight:500;display:flex;align-items:center;justify-content:center;border-radius:0 3px 3px 0}
.nav{left:664px;top:43px;display:flex;gap:4px;font-size:12px;color:#ddd}
.nav a{color:inherit;text-decoration:none;padding:4px 5px}
.nav a.active{background:var(--yellow);color:#222;border-radius:2px}
.hero-title{left:0;top:146px;width:1200px;text-align:center;color:var(--yellow);font-size:29px;font-weight:500}
.hero-lead{left:0;top:194px;width:1200px;text-align:center;color:#fff;font-size:11px;font-weight:500;line-height:17px}
.btn-search{left:549px;top:257px;width:104px;height:33px;background:var(--cyan);color:#fff;font-size:11px;font-weight:500;display:flex;align-items:center;justify-content:center;gap:5px;border-radius:2px}
.tab{height:40px;border:2px solid var(--yellow);border-bottom:none;color:var(--cyan);font-family:'Oswald',sans-serif;font-size:16px;display:flex;align-items:center;justify-content:center;background:rgba(0,0,0,.25)}
.tab-rent{left:266px;top:356px;width:238px}
.tab-house{left:696px;top:356px;width:238px}
.card{top:396px;width:183px;height:156px;background:#333;overflow:hidden}
.card .label{position:absolute;left:0;top:0;width:100%;height:34px;background:var(--yellow);color:#222;font-family:'Oswald',sans-serif;font-size:11px;text-align:center;padding-top:7px;border-radius:0 0 50% 50%/0 0 40% 40%;z-index:1}
.card .photo{position:absolute;left:0;top:0;width:100%;height:100%;background:linear-gradient(160deg,#8c7b66 0%,#c9b59b 45%,#e8e2d8 70%,#6f6a63 100%)}
.card .photo.alt{background:linear-gradient(160deg,#6b5e52 0%,#b8a792 40%,#f0ece6 70%,#8a8580 100%)}
.card.info{background:#fff}
.card.info .label{height:98px;padding:6px 10px;font-size:11px}
.card.info .label p{font-family:'Roboto',sans-serif;font-size:9.5px;line-height:13px;margin-top:5px}
.c1{left:189px}.c2{left:398px}.c3{left:620px}.c4{left:828px}
.hero-wave{left:0;top:548px;width:1200px;height:50px}

/* SPOTLIGHT */
.spotlight{left:0;top:596px;width:1200px;height:554px;background:linear-gradient(180deg,#eeeeee 0%,#fff 30%)}
.spot-title{top:640px;width:440px;text-align:center;color:var(--cyan-dark);font-size:23px}
.st1{left:160px}.st2{left:600px}
.member{top:703px;width:200px;height:339px}
.member .base{position:absolute;left:0;top:108px;width:100%;height:231px}
.member.yellow .base{background:var(--yellow)}
.member.cyan .base{background:var(--cyan)}
.member .hex{position:absolute;left:8px;top:0;width:184px;height:217px;clip-path:polygon(50% 0,100% 22%,100% 78%,50% 100%,0 78%,0 22%);background:#fff}
.member .hex i{position:absolute;inset:3px;clip-path:polygon(50% 0,100% 22%,100% 78%,50% 100%,0 78%,0 22%)}
.member.people .hex i{background:linear-gradient(180deg,#7fb3d9 0%,#c79a6e 55%,#5b4a3c 100%)}
.member.house .hex i{background:linear-gradient(180deg,#9fc4e6 0%,#e9e4dc 55%,#6d6560 100%)}
.member.room .hex i{background:linear-gradient(180deg,#d8dde2 0%,#f3f3f1 55%,#a9a8a2 100%)}
.member h3{position:absolute;top:222px;width:100%;text-align:center;font-family:'Roboto',sans-serif;font-weight:500;font-size:14px;color:#222}
.member p{position:absolute;top:251px;width:100%;text-align:center;font-size:11px;line-height:17px;color:#333}
.member.cyan h3,.member.cyan p{color:#fff}
.m1{left:170px}.m2{left:387px}.m3{left:611px}.m4{left:828px}
.btn-more{top:1078px;width:120px;height:35px;font-family:'Oswald',sans-serif;font-size:12px;display:flex;align-items:center;justify-content:center;gap:5px;border-radius:2px}
.bm1{left:309px;background:var(--yellow);color:#222}
.bm2{left:762px;background:var(--cyan);color:#fff}

/* SELLING POINTS */
.selling{left:0;top:1150px;width:1200px;height:371px;background:linear-gradient(180deg,#34475a 0%,#27323f 55%,#1f2630 100%)}
.point{top:1224px;width:407px;height:223px;border:1px solid var(--cyan);padding:30px 14px;text-align:center}
.point h2{color:var(--yellow);font-size:18px;margin-bottom:20px}
.point p{color:#fff;font-size:10.5px;line-height:18.5px;font-weight:500}
.p1{left:179px}.p2{left:613px}

/* KNOW ABOUT */
.know-photo{left:600px;top:1577px;width:600px;height:500px;background:linear-gradient(120deg,#c9b8a4 0%,#e8dccd 35%,#9a8270 65%,#5d4a3d 100%)}
.know-panel{left:0;top:1577px;width:660px;height:500px}
.know-title{left:170px;top:1640px;font-size:19px;color:#222;font-weight:500}
.faq{left:170px;width:420px;font-size:11px;line-height:17.5px;color:#222}
.faq b{font-weight:700}
.faq .read{display:flex;align-items:center;gap:4px;font-size:10px;font-weight:700;margin-top:3px}
.faq-rule{left:330px;width:250px;height:1px;background:rgba(0,0,0,.15)}
.f1{top:1707px}.f2{top:1827px}.f3{top:1947px}

/* TAB BAND */
.band{left:0;top:2130px;width:1200px;height:86px}
.band-text{top:2168px;font-family:'Oswald',sans-serif;font-size:18px}
.bt1{left:303px;color:#fff}
.bt2{left:722px;color:#111}

/* FOOTER */
.footer{left:0;top:2214px;width:1200px;height:294px;background:linear-gradient(180deg,#202226 0%,#17181a 100%)}
.foot-head{top:2280px;color:var(--yellow);font-size:17px}
.fh1{left:170px;top:2283px}.fh2{left:450px;top:2267px}.fh3{left:748px;top:2267px}
.foot-text{width:215px;color:#fff;font-size:10.5px;line-height:19px}
.ft1{left:170px;top:2330px}.ft2{left:450px;top:2325px}
.gallery{left:748px;top:2334px;display:grid;grid-template-columns:repeat(4,55px);grid-template-rows:repeat(2,55px);gap:8px}
.gallery i{display:block}
.g1{background:linear-gradient(135deg,#6f6a5f,#b3a58b)}
.g2{background:linear-gradient(135deg,#2b5d7a,#c88a4f)}
.g3{background:linear-gradient(135deg,#1f5f6e,#d9553b)}
.g4{background:linear-gradient(135deg,#33435a,#e0a46d)}
.g5{background:linear-gradient(135deg,#6e7f5c,#c7c0b0)}
.g6{background:linear-gradient(135deg,#4a8fb3,#e8d7b8)}
.g7{background:linear-gradient(135deg,#2a2b3a,#e0b15a)}
.g8{background:linear-gradient(135deg,#34405e,#f0a766)}
.foot-bar{left:0;top:2508px;width:1200px;height:62px;background:var(--darker)}
.foot-nav{left:170px;top:2530px;display:flex;gap:16px;font-size:11px;color:#666}
.foot-nav a{color:inherit;text-decoration:none}
.foot-nav a.active{color:var(--yellow)}
.foot-brand{left:946px;top:2530px;display:flex;align-items:center;gap:6px;color:#fff;font-weight:700;font-size:13px}
.copyright{left:0;top:2570px;width:1200px;height:35px;background:var(--cyan);color:#fff;font-size:11px;display:flex;align-items:center;justify-content:center}
</style>
</head>
<body>

<!-- HERO -->
<section class="abs hero" role="img" aria-label="Dim city street photograph behind the hero"></section>
<header class="abs topbar"></header>
<div class="abs brand"><span class="brand-dot"></span>Lantern Nest Place</div>
<div class="abs social" aria-label="Social links"><span></span><span></span><span></span><span></span></div>
<div class="abs btn-create">Create</div>
<div class="abs btn-login">Login</div>
<nav class="abs nav">
  <a class="active" href="#">HOME</a><a href="#">GROUP</a><a href="#">PROPERTIES</a><a href="#">SALES CONDITIONS</a><a href="#">MY ACCOUNT</a>
</nav>
<h1 class="abs hero-title">Flatshring for Everyone !</h1>
<p class="abs hero-lead">Lorem Ipsum is simply dummy text of the printing and typesetting industry.<br>Lorem Ipsum has been the industry's standard dummy text ever since the 1500s,<br>when an unknown printer took a galley of type</p>
<div class="abs btn-search">Search Now
  <svg width="10" height="10" viewBox="0 0 10 10"><circle cx="4" cy="4" r="3" fill="none" stroke="#fff" stroke-width="1.5"/><line x1="6.2" y1="6.2" x2="9" y2="9" stroke="#fff" stroke-width="1.5"/></svg>
</div>

<div class="abs tab tab-rent">Searching for accommodation</div>
<div class="abs tab tab-house">I have a house for rent</div>

<div class="abs card c1"><div class="label">I want ti rent a room right now !</div><div class="photo" role="img" aria-label="Hotel-style bedroom with a window view"></div></div>
<div class="abs card c2"><div class="label">I want to join a group</div><div class="photo alt" role="img" aria-label="Bright bedroom with twin beds"></div></div>
<div class="abs card c3"><div class="label">I WANT TO ADVERTISE !</div><div class="photo" role="img" aria-label="Bedroom with city view"></div></div>
<div class="abs card c4 info"><div class="label">Why is flatsharing interesting fo me ?<p>Lorem Ipsum is simply dummy text of the printing and typesetting industry. Lorem Ipsum has been the industry's</p></div><div class="photo alt" role="img" aria-label="Modern bedroom interior"></div></div>

<svg class="abs hero-wave" viewBox="0 0 1200 50" preserveAspectRatio="none" aria-hidden="true">
  <path d="M0 20 Q300 30 600 14 Q900 0 1200 22 L1200 50 L0 50 Z" fill="var(--cyan)"/>
</svg>

<!-- SPOTLIGHT -->
<section class="abs spotlight"></section>
<h2 class="abs spot-title st1">Under the spotlight</h2>
<h2 class="abs spot-title st2">Under the spotlight</h2>

<article class="abs member yellow people m1"><div class="base"></div><div class="hex"><i role="img" aria-label="Group of young friends at the beach"></i></div><h3>A NICE GROUP</h3><p>young worker, seeking for<br>accomodation downtown.<br>Average age : 35 years<br>Men and women welcome</p></article>
<article class="abs member yellow people m2"><div class="base"></div><div class="hex"><i role="img" aria-label="Group of smiling young people"></i></div><h3>A NICE GROUP</h3><p>young worker, seeking for<br>accomodation downtown.<br>Average age : 35 years<br>Men and women welcome</p></article>
<article class="abs member cyan house m3"><div class="base"></div><div class="hex"><i role="img" aria-label="Two-storey house exterior"></i></div><h3>A NICE GROUP</h3><p>young worker, seeking for<br>accomodation downtown.<br>Average age : 35 years<br>Men and women welcome</p></article>
<article class="abs member cyan room m4"><div class="base"></div><div class="hex"><i role="img" aria-label="Bright modern living room"></i></div><h3>A NICE GROUP</h3><p>young worker, seeking for<br>accomodation downtown.<br>Average age : 35 years<br>Men and women welcome</p></article>

<div class="abs btn-more bm1">See More Groups <svg width="9" height="9" viewBox="0 0 9 9"><path d="M0 4.5H7M4 1.5L7 4.5L4 7.5" fill="none" stroke="#222" stroke-width="1.6"/></svg></div>
<div class="abs btn-more bm2">See More Groups <svg width="9" height="9" viewBox="0 0 9 9"><path d="M0 4.5H7M4 1.5L7 4.5L4 7.5" fill="none" stroke="#fff" stroke-width="1.6"/></svg></div>

<!-- SELLING POINTS -->
<section class="abs selling" role="img" aria-label="Dark blue-toned open-plan living room photograph"></section>
<div class="abs point p1"><h2>Key Selling Points for the Roommates</h2><p>Lorem Ipsum is simply dummy text of the printing and typesetting industry. Lorem Ipsum has been the industry's standard dummy text ever since the 1500s, when an unknown printer took a galley of type and scrambled it to make a type specimen book. It has survived not only Lorem Ipsum is simply dummy text of the printing and typesetting industry. Lorem Ipsum has been the industry's standard dummy text ever since the 1500s, when an unknown printer took a</p></div>
<div class="abs point p2"><h2>Key Selling Points for the Owners</h2><p>Lorem Ipsum is simply dummy text of the printing and typesetting industry. Lorem Ipsum has been the industry's standard dummy text ever since the 1500s, when an unknown printer took a galley of type and scrambled it to make a type specimen book. It has survived not only Lorem Ipsum is simply dummy text of the printing and typesetting industry. Lorem Ipsum has been the industry's standard dummy text ever since the 1500s, when an unknown printer took a</p></div>

<!-- KNOW ABOUT -->
<div class="abs know-photo" role="img" aria-label="Friends laughing together at a café table"></div>
<svg class="abs know-panel" viewBox="0 0 660 500" preserveAspectRatio="none" aria-hidden="true">
  <polygon points="0,0 656,0 620,500 0,500" fill="var(--yellow-soft)"/>
</svg>
<h2 class="abs know-title">Everything You need to know About Flatshring</h2>
<div class="abs faq f1"><b>1.</b>Lorem Ipsum is simply dummy text of the printing and typesetting industry. Lorem Ipsum has been the industry's standard dummy text ever since the 1500s, when an unknown printer took a galley of type and scrambled it to make a type<div class="read">READ MORE <svg width="8" height="8" viewBox="0 0 9 9"><path d="M0 4.5H7M4 1.5L7 4.5L4 7.5" fill="none" stroke="#222" stroke-width="1.8"/></svg></div></div>
<div class="abs faq-rule" style="top:1805px"></div>
<div class="abs faq f2"><b>2.</b>Lorem Ipsum is simply dummy text of the printing and typesetting industry. Lorem Ipsum has been the industry's standard dummy text ever since the 1500s, when an unknown printer took a galley of type and scrambled it to make a type<div class="read">READ MORE <svg width="8" height="8" viewBox="0 0 9 9"><path d="M0 4.5H7M4 1.5L7 4.5L4 7.5" fill="none" stroke="#222" stroke-width="1.8"/></svg></div></div>
<div class="abs faq-rule" style="top:1925px"></div>
<div class="abs faq f3"><b>3.</b>Lorem Ipsum is simply dummy text of the printing and typesetting industry. Lorem Ipsum has been the industry's standard dummy text ever since the 1500s, when an unknown printer took a galley of type and scrambled it to make a type<div class="read">READ MORE <svg width="8" height="8" viewBox="0 0 9 9"><path d="M0 4.5H7M4 1.5L7 4.5L4 7.5" fill="none" stroke="#222" stroke-width="1.8"/></svg></div></div>

<!-- TAB BAND -->
<svg class="abs band" viewBox="0 0 1200 86" preserveAspectRatio="none" aria-hidden="true">
  <polygon points="0,34 600,3 600,86 0,86" fill="var(--cyan)"/>
  <polygon points="600,3 1200,34 1200,86 600,86" fill="var(--yellow)"/>
</svg>
<div class="abs band-text bt1">PRE-DEFINED SEARCHES</div>
<div class="abs band-text bt2">TOOLS AND INFORMATIONS</div>

<!-- FOOTER -->
<footer class="abs footer" role="img" aria-label="Dark night city skyline photograph"></footer>
<h3 class="abs foot-head fh1">Come Visit Us</h3>
<h3 class="abs foot-head fh2">More About Us</h3>
<h3 class="abs foot-head fh3">Snapshot Feed</h3>
<p class="abs foot-text ft1">Lorem Ipsum is simply dummy text of the printing and typesetting industry. Lorem Ipsum has been the industry's standard dummy text ever since the 1500s, when an unknown printer took a galley of type andLorem Ipsum is simply dummy text of the printing and typesetting</p>
<p class="abs foot-text ft2">Lorem Ipsum is simply dummy text of the printing and typesetting industry. Lorem Ipsum has been the industry's standard dummy text ever since the 1500s, when an unknown printer took a galley of type andLorem Ipsum is simply dummy text of the printing and typesetting industry. Lorem Ipsum has</p>
<div class="abs gallery">
  <i class="g1" role="img" aria-label="Street scene thumbnail"></i>
  <i class="g2" role="img" aria-label="Travel thumbnail"></i>
  <i class="g3" role="img" aria-label="Nature thumbnail"></i>
  <i class="g4" role="img" aria-label="Sunset thumbnail"></i>
  <i class="g5" role="img" aria-label="Landscape thumbnail"></i>
  <i class="g6" role="img" aria-label="Coast thumbnail"></i>
  <i class="g7" role="img" aria-label="Evening lights thumbnail"></i>
  <i class="g8" role="img" aria-label="Dusk sky thumbnail"></i>
</div>
<div class="abs foot-bar"></div>
<nav class="abs foot-nav"><a class="active" href="#">Home</a><a href="#">Group</a><a href="#">Properties</a><a href="#">Sales conditions</a><a href="#">My account</a><a href="#">Contact</a></nav>
<div class="abs foot-brand"><span class="brand-dot"></span>Lantern Nest Place</div>
<div class="abs copyright">Copyright © 2016 Lantern Nest Place</div>

</body>
</html>
```